New flyer design for construction company marketing and description of services.

I want to have a flyer design that my techs will carry to deliver after job completion or for marketing purposes, to explain what services we provide, we offer General construction services.

Brellor Homecraft Sevices originated from a family-owned and operated contractor business, performing home renovation, addition, and construction work in the NYC area since 2004.

Today, we specialize in reliable and affordable Construction services for residential and commercial clients In 2014, we expanded to northern New Jersey. In 2016, we brought quality home improvement and repair services to new Bucks County, PA, and nearby New Jersey areas.
We offer carpentry, electrical, plumbing, renovation, remodel, cleaning services and landscaping.
I would like to have a section for home rental maintenance.

Target Market(s)

Homeowners, rental properties, real state and Senior citizen

Industry/Entity Type

Construction Company

Colors

Designer to choose colors to be used in the design.

Requirements
Must have
• A special design that will attract 55 + clients maybe a logo version that will be more attractive to seniors. I would updated the briefing with design and previous pictures, but we have all available in our social media instagram and facebook:
• https://www.pictogram.example/brellorhomecraft/?hl=en
• https://www.friendsbook.example/brellorhome/
Nice to have
• New design ideas and layouts.

```html
<!DOCTYPE html>
<html lang="en">
<head>
<meta charset="utf-8">
<title>Brellor Homecraft Services – Flyers</title>
<link rel="stylesheet" href="https://fonts.googleapis.com/css2?family=Bebas+Neue&family=Oswald:wght@600&family=Open+Sans:wght@400;600;700&display=swap">
<style>
:root{
  --red:#e3262b;
  --navy:#211e5c;
  --ink:#18181f;
  --dark:#1a1a22;
  --yellow:#f6c619;
  --panel:#e3e4ea;
  --page:#f2f2f4;
  --bg:#d9d6d2;
  --white:#ffffff;
}
*{margin:0;padding:0;box-sizing:border-box}
html,body{width:1200px;height:775px;overflow:hidden;background:var(--bg)}
.canvas{position:relative;width:1200px;height:775px}
.flyer-slot{position:absolute;top:30px;width:552px;height:715px;box-shadow:0 6px 16px rgba(0,0,0,.25)}
.flyer-slot.left{left:30px}
.flyer-slot.right{left:618px}
.flyer{position:absolute;top:0;left:0;width:612px;height:792px;transform:scale(.9028);transform-origin:0 0;background:var(--white);overflow:hidden;font-family:"Open Sans",sans-serif;color:var(--navy)}
.flyer-art{position:absolute;inset:0}
.brand{position:absolute;left:24px;top:60px;display:flex;align-items:center;gap:12px}
.brand-dot{width:40px;height:40px;border-radius:50%;background:var(--red)}
.brand-name{font-family:"Oswald",sans-serif;font-weight:600;font-size:32px;color:var(--navy);letter-spacing:.5px}
.headline{position:absolute;left:20px;top:200px;font-family:"Bebas Neue",sans-serif;font-weight:400;font-size:54px;line-height:52px;color:var(--red);text-transform:uppercase}
.subline{position:absolute;left:20px;top:313px;font-size:15.5px;line-height:19px;color:var(--navy)}
.subline.caps{text-transform:uppercase}
.intro{position:absolute;left:22px;top:416px;width:570px;font-size:10.6px;line-height:17px;font-weight:600;color:var(--ink);text-align:justify}
.service-grid{position:absolute;left:22px;top:523px;width:570px;height:192px;background:var(--panel);display:grid;grid-template-columns:1fr 1fr;grid-template-rows:1fr 1fr}
.service{display:flex;gap:14px;padding:12px 10px 0 8px;border-color:#9a9aa6;border-style:dotted;border-width:0}
.service:nth-child(1){border-right-width:1.5px;border-bottom-width:1.5px}
.service:nth-child(2){border-bottom-width:1.5px}
.service:nth-child(3){border-right-width:1.5px}
.service svg{flex:none;width:66px;height:68px}
.service h3{font-family:"Bebas Neue",sans-serif;font-weight:400;font-size:21px;color:var(--red);text-transform:uppercase;line-height:24px}
.service p{font-size:8.2px;line-height:10px;color:var(--navy);text-align:justify;margin-top:2px}
.footer-mail{position:absolute;left:22px;top:764px;width:330px;white-space:nowrap;font-size:13.5px;font-weight:600;color:var(--ink)}
.footer-phone{position:absolute;left:380px;top:748px;display:flex;align-items:center;gap:14px;color:var(--white);font-size:24px}
.offer-title{position:absolute;left:20px;top:410px;font-family:"Bebas Neue",sans-serif;font-weight:400;font-size:33px;color:var(--navy)}
.offer-list{position:absolute;left:20px;top:456px;list-style:none}
.offer-list li{display:flex;align-items:center;gap:10px;height:23.5px;font-size:15.5px;color:var(--navy)}
.offer-list svg{width:16px;height:16px}
.gallery{position:absolute;left:274px;top:410px;display:grid;grid-template-columns:154px 154px;grid-auto-rows:98px;column-gap:7px;row-gap:12px}
.shot{position:relative;overflow:hidden;border:2px solid var(--white);box-shadow:0 0 0 1px #c9c9d0}
.shot.before{background:linear-gradient(135deg,#8c7a68,#c8b9a4 55%,#6d5a4a)}
.shot.after{background:linear-gradient(135deg,#6e2e22,#c9a27a 50%,#f1e6d4)}
.shot.dark.before{background:linear-gradient(135deg,#3a3a44,#8e8a86 55%,#2a2a30)}
.shot.dark.after{background:linear-gradient(135deg,#5d5e62,#d8d9dc 55%,#3a3b40)}
.tag{position:absolute;left:-24px;top:10px;width:96px;transform:rotate(-35deg);background:var(--red);color:var(--white);font-family:"Bebas Neue",sans-serif;font-size:12px;text-align:center;line-height:14px}
</style>
</head>
<body>
<div class="canvas">

  <!-- Company overview flyer -->
  <div class="flyer-slot left">
    <article class="flyer">
      <svg class="flyer-art" viewBox="0 0 612 792" width="612" height="792">
        <defs>
          <linearGradient id="worker-photo" x1="0" y1="0" x2="1" y2="1">
            <stop offset="0" stop-color="#e8e2da"/>
            <stop offset=".55" stop-color="#b9ad9f"/>
            <stop offset="1" stop-color="#2b2c4f"/>
          </linearGradient>
        </defs>
        <rect x="0" y="398" width="612" height="340" fill="var(--page)"/>
        <g role="img" aria-label="Photo of a smiling handyman in a hard hat with crossed arms and work gloves">
          <polygon points="290,22 612,22 612,398 270,398" fill="url(#worker-photo)"/>
        </g>
        <polygon points="0,142 300,142 310,180 0,180" fill="var(--dark)"/>
        <polygon points="0,180 340,180 385,372 0,372" fill="var(--white)"/>
        <polygon points="0,372 385,372 392,398 0,398" fill="var(--dark)"/>
        <rect x="0" y="748" width="380" height="44" fill="var(--yellow)"/>
        <line x1="0" y1="752" x2="370" y2="752" stroke="#d9a90a" stroke-width="2"/>
        <polygon points="365,735 612,735 612,792 348,792" fill="var(--dark)"/>
      </svg>

      <div class="brand"><span class="brand-dot"></span><span class="brand-name">Brellor Homecraft</span></div>

      <h1 class="headline">A Better Way<br>To Get Task Done</h1>
      <p class="subline">Licensed Home Improvement Contractor in<br>PA 000000 and NJ 00XX00000000</p>

      <p class="intro">Brellor Homecraft Sevices originated from a family-owned and operated contractor business, performing home renovation, addition, and construction work in the NYC area since 2004. Today, we specialize in reliable and affordable Construction services for residential and commercial clients In 2014, we expanded to northern New Jersey. In 2016, we brought quality home improvement and repair services to new Bucks County, PA, and nearby New Jersey areas.</p>

      <div class="service-grid">
        <div class="service">
          <svg viewBox="0 0 66 68"><polygon points="17,4 49,4 64,34 49,64 17,64 2,34" fill="var(--white)" stroke="var(--navy)" stroke-width="2"/><circle cx="33" cy="27" r="9" fill="var(--red)"/><path d="M18 50 q15 -16 30 0z" fill="var(--red)"/></svg>
          <div><h3>General Contractor</h3><p>We are committed to our clients in offering them products and services of first-class quality, within the timelines and budgets agreed.</p></div>
        </div>
        <div class="service">
          <svg viewBox="0 0 66 68"><polygon points="17,4 49,4 64,34 49,64 17,64 2,34" fill="var(--white)" stroke="var(--navy)" stroke-width="2"/><rect x="20" y="24" width="16" height="22" rx="2" fill="var(--red)"/><path d="M40 20 l6 14 h-6z" fill="var(--red)"/><line x1="44" y1="34" x2="44" y2="48" stroke="var(--red)" stroke-width="3"/></svg>
          <div><h3>Cleaning Services</h3><p>If you're in need of home cleaning, apartment cleaning, or a maid service, we're simply the best, most convenient home cleaning service out there.</p></div>
        </div>
        <div class="service">
          <svg viewBox="0 0 66 68"><polygon points="17,4 49,4 64,34 49,64 17,64 2,34" fill="var(--white)" stroke="var(--navy)" stroke-width="2"/><path d="M33 16 l18 16 h-5 v16 h-26 v-16 h-5z" fill="var(--red)"/><path d="M27 34 l12 10 M39 34 l-12 10" stroke="var(--white)" stroke-width="3"/></svg>
          <div><h3>Property Maintenance</h3><p>Whether your facility is large or small, we are responsible for fixing damage and replacing equipment, as well as replenishing any supplies necessary for the efficient operation of the property.</p></div>
        </div>
        <div class="service">
          <svg viewBox="0 0 66 68"><polygon points="17,4 49,4 64,34 49,64 17,64 2,34" fill="var(--white)" stroke="var(--navy)" stroke-width="2"/><circle cx="28" cy="38" r="9" fill="none" stroke="var(--red)" stroke-width="6" stroke-dasharray="4 3"/><circle cx="42" cy="24" r="6" fill="none" stroke="var(--red)" stroke-width="4" stroke-dasharray="3 2"/></svg>
          <div><h3>Handyman Services</h3><p>If you're looking for the best handyman service to help you out around the house, look no further. We know you've got a never-ending list of odd jobs that need doing around your home.</p></div>
        </div>
      </div>

      <p class="footer-mail">brellor@mail.example | www.brellor.example</p>
      <div class="footer-phone">
        <svg width="30" height="30" viewBox="0 0 30 30"><circle cx="15" cy="15" r="13" fill="none" stroke="var(--white)" stroke-width="2"/><path d="M10 8 c-2 2 -1 6 3 10 s8 5 10 3 l-3 -3 -2 2 c-2 -1 -4 -3 -5 -5 l2 -2z" fill="var(--white)"/></svg>
        <span>(555) 014-3415</span>
      </div>
    </article>
  </div>

  <!-- Services and projects flyer -->
  <div class="flyer-slot right">
    <article class="flyer">
      <svg class="flyer-art" viewBox="0 0 612 792" width="612" height="792">
        <defs>
          <linearGradient id="tools-photo" x1="0" y1="0" x2="1" y2="1">
            <stop offset="0" stop-color="#d8cfc4"/>
            <stop offset=".5" stop-color="#a9998a"/>
            <stop offset="1" stop-color="#1f2438"/>
          </linearGradient>
        </defs>
        <rect x="0" y="398" width="612" height="340" fill="var(--page)"/>
        <g role="img" aria-label="Photo of a worker's tool belt with a hammer, wrenches and a hard hat in front of a house entrance">
          <polygon points="290,22 612,22 612,398 270,398" fill="url(#tools-photo)"/>
        </g>
        <polygon points="0,142 300,142 310,180 0,180" fill="var(--dark)"/>
        <polygon points="0,180 340,180 385,372 0,372" fill="var(--white)"/>
        <polygon points="0,372 385,372 392,398 0,398" fill="var(--dark)"/>
        <rect x="0" y="748" width="380" height="44" fill="var(--yellow)"/>
        <line x1="0" y1="752" x2="370" y2="752" stroke="#d9a90a" stroke-width="2"/>
        <polygon points="365,735 612,735 612,792 348,792" fill="var(--dark)"/>
      </svg>

      <div class="brand"><span class="brand-dot"></span><span class="brand-name">Brellor Homecraft</span></div>

      <h1 class="headline">Brellor Homecraft<br>Services</h1>
      <p class="subline caps">Call the pros, not the cons<br>We do it all, large and small</p>

      <h2 class="offer-title">SERVICES WE OFFER</h2>
      <ul class="offer-list">
        <li><svg viewBox="0 0 16 16"><rect x="1" y="3" width="12" height="12" fill="none" stroke="var(--red)" stroke-width="1.6"/><path d="M4 8 l3 3 l8 -9" fill="none" stroke="var(--red)" stroke-width="2"/></svg>CARPENTRY</li>
        <li><svg viewBox="0 0 16 16"><rect x="1" y="3" width="12" height="12" fill="none" stroke="var(--red)" stroke-width="1.6"/><path d="M4 8 l3 3 l8 -9" fill="none" stroke="var(--red)" stroke-width="2"/></svg>ELECTRICAL</li>
        <li><svg viewBox="0 0 16 16"><rect x="1" y="3" width="12" height="12" fill="none" stroke="var(--red)" stroke-width="1.6"/><path d="M4 8 l3 3 l8 -9" fill="none" stroke="var(--red)" stroke-width="2"/></svg>PLUMBING</li>
        <li><svg viewBox="0 0 16 16"><rect x="1" y="3" width="12" height="12" fill="none" stroke="var(--red)" stroke-width="1.6"/><path d="M4 8 l3 3 l8 -9" fill="none" stroke="var(--red)" stroke-width="2"/></svg>RENOVATION</li>
        <li><svg viewBox="0 0 16 16"><rect x="1" y="3" width="12" height="12" fill="none" stroke="var(--red)" stroke-width="1.6"/><path d="M4 8 l3 3 l8 -9" fill="none" stroke="var(--red)" stroke-width="2"/></svg>REMODEL</li>
        <li><svg viewBox="0 0 16 16"><rect x="1" y="3" width="12" height="12" fill="none" stroke="var(--red)" stroke-width="1.6"/><path d="M4 8 l3 3 l8 -9" fill="none" stroke="var(--red)" stroke-width="2"/></svg>CLEANING SERVICES</li>
        <li><svg viewBox="0 0 16 16"><rect x="1" y="3" width="12" height="12" fill="none" stroke="var(--red)" stroke-width="1.6"/><path d="M4 8 l3 3 l8 -9" fill="none" stroke="var(--red)" stroke-width="2"/></svg>LANDSCAPING</li>
        <li><svg viewBox="0 0 16 16"><rect x="1" y="3" width="12" height="12" fill="none" stroke="var(--red)" stroke-width="1.6"/><path d="M4 8 l3 3 l8 -9" fill="none" stroke="var(--red)" stroke-width="2"/></svg>MAINTENANCE</li>
        <li><svg viewBox="0 0 16 16"><rect x="1" y="3" width="12" height="12" fill="none" stroke="var(--red)" stroke-width="1.6"/><path d="M4 8 l3 3 l8 -9" fill="none" stroke="var(--red)" stroke-width="2"/></svg>PAINTING</li>
        <li><svg viewBox="0 0 16 16"><rect x="1" y="3" width="12" height="12" fill="none" stroke="var(--red)" stroke-width="1.6"/><path d="M4 8 l3 3 l8 -9" fill="none" stroke="var(--red)" stroke-width="2"/></svg>WOOD TRIM</li>
        <li><svg viewBox="0 0 16 16"><rect x="1" y="3" width="12" height="12" fill="none" stroke="var(--red)" stroke-width="1.6"/><path d="M4 8 l3 3 l8 -9" fill="none" stroke="var(--red)" stroke-width="2"/></svg>TILE</li>
        <li><svg viewBox="0 0 16 16"><rect x="1" y="3" width="12" height="12" fill="none" stroke="var(--red)" stroke-width="1.6"/><path d="M4 8 l3 3 l8 -9" fill="none" stroke="var(--red)" stroke-width="2"/></svg>REPAIR</li>
      </ul>

      <div class="gallery">
        <div class="shot before" role="img" aria-label="Kitchen before renovation, cabinets removed"><span class="tag">BEFORE</span></div>
        <div class="shot after" role="img" aria-label="Kitchen after renovation with new wood cabinets"><span class="tag">AFTER</span></div>
        <div class="shot dark before" role="img" aria-label="Balcony doors before repair"><span class="tag">BEFORE</span></div>
        <div class="shot dark after" role="img" aria-label="Balcony after repair with new railing"><span class="tag">AFTER</span></div>
        <div class="shot before" role="img" aria-label="Basement before remodel with exposed studs"><span class="tag">BEFORE</span></div>
        <div class="shot after" role="img" aria-label="Finished basement after remodel with bar area"><span class="tag">AFTER</span></div>
      </div>

      <p class="footer-mail">brellor@mail.example | www.brellor.example</p>
      <div class="footer-phone">
        <svg width="30" height="30" viewBox="0 0 30 30"><circle cx="15" cy="15" r="13" fill="none" stroke="var(--white)" stroke-width="2"/><path d="M10 8 c-2 2 -1 6 3 10 s8 5 10 3 l-3 -3 -2 2 c-2 -1 -4 -3 -5 -5 l2 -2z" fill="var(--white)"/></svg>
        <span>(555) 014-3415</span>
      </div>
    </article>
  </div>

</div>
</body>
</html>
```